Banners for hosting service

TO BID, PUBLISH A SAMPLE BANNER IS ENOUGH

We need some banners for our site [login to view URL], to promote Virtual Private Servers, Dedicated Servers and Shared Hosting. You CAN use our attached format (pixelmarten file) or use own.

Sizes: 300x600, 300x250, 728x90, 160x600, 336x280, 970x250, 468x60, 250x250, 200x200
Limit initial load size to 40 KB or less
Limit animation to 30 seconds
Limit animation to 3 loops max
Use standard click variable clickTAG
1 pixel colored border required
Avoid auto-initiated audio
No auto-expansion or page takeovers
Flash Player Version 8 or lower is ideal
Compile Flash ads in ActionScript 2 or 3
Do not serve blanks

Necessary to include the company logo (attached). And a better datacenter image, if possible (sample attached as "hosting")

Will be 3 sets, with all indicated sizes each one.

SET 1: Main text: "Virtual Private Servers", "from $5/mo"
Other texts: "Locations: USA, Germany, France, UK, Spain, Canada..." (can be icon flags)
Features list: "Linux and Windows - 24/7 Free support - All panels - Root Access - High speed - Uptime 99.9% - Instant Setup - Dedicated Bandwidth"
Then a button "Click here" to invite to click in banner

SET 2: Main text: "Dedicated Servers", "from $49/mo"
Features list: "Linux and Windows - 24/7 Free support - Free panels - Root Access - High speed - Uptime 99.9% - Instant Setup - KVM"

SET 3: Main text: "Shared Web Hosting", "Only 0.99 per mo"
Features list: "24/7 Free support - Free cPanel - High speed - Uptime 99.9% - Instant Setup - Webmail".

```html
<!DOCTYPE html>
<html lang="en">
<head>
<meta charset="utf-8">
<title>Virtual Private Servers banner</title>
<link rel="stylesheet" href="https://fonts.googleapis.com/css2?family=Roboto:wght@400&family=Roboto+Condensed:wght@400;700&family=Oleo+Script&display=swap">
<style>
  :root {
    --backdrop: #76777b;
    --banner-dark: #050505;
    --banner-mid: #1c1c1c;
    --headline: #f6cc3c;
    --features: #e4e4e4;
    --price-red: #b0141a;
    --price-shadow: #5a0608;
    --sticker-light: #ffffff;
    --sticker-shade: #c9c9c9;
    --button-top: #a41c20;
    --button-bottom: #4e0507;
    --flag-white: #ffffff;
    --flag-red: #d22730;
    --flag-blue: #1f3a8a;
    --flag-navy: #012169;
    --flag-black: #111111;
    --flag-gold: #ffce00;
    --flag-french-blue: #0055a4;
    --flag-french-red: #ef4135;
    --flag-spain-red: #c60b1e;
    --flag-spain-yellow: #ffc400;
  }
  html, body {
    margin: 0;
    padding: 0;
    width: 1200px;
    height: 240px;
    overflow: hidden;
    background: var(--backdrop);
  }
  .banner {
    position: absolute;
    left: 32px;
    top: 50px;
    width: 1136px;
    height: 140px;
    overflow: hidden;
    background: radial-gradient(ellipse at 62% 50%, var(--banner-mid) 0%, var(--banner-dark) 70%);
  }
  .banner__texture {
    position: absolute;
    inset: 0;
    background: linear-gradient(90deg, rgba(255,255,255,0.03), rgba(255,255,255,0.06) 60%, rgba(255,255,255,0.02));
  }
  .headline {
    position: absolute;
    left: 52px;
    top: 6px;
    margin: 0;
    font-family: "Roboto", sans-serif;
    font-weight: 400;
    font-size: 50px;
    line-height: 60px;
    letter-spacing: 0.3px;
    color: var(--headline);
    white-space: nowrap;
  }
  .features {
    position: absolute;
    left: 50px;
    top: 79px;
    margin: 0;
    font-family: "Roboto Condensed", sans-serif;
    font-weight: 400;
    font-size: 15.5px;
    line-height: 29px;
    color: var(--features);
    white-space: nowrap;
  }
  .sticker {
    position: absolute;
    left: 618px;
    top: 22px;
    width: 112px;
    height: 112px;
  }
  .price__from {
    position: absolute;
    left: 606px;
    top: 4px;
    font-family: "Oleo Script", cursive;
    font-size: 26px;
    color: var(--price-red);
    transform: rotate(-10deg);
    text-shadow: 1px 1px 0 var(--price-shadow);
  }
  .price__amount {
    position: absolute;
    left: 626px;
    top: 46px;
    font-family: "Roboto Condensed", sans-serif;
    font-weight: 700;
    font-size: 48px;
    line-height: 56px;
    color: var(--price-red);
    letter-spacing: -1px;
    text-shadow: 1px 2px 0 var(--price-shadow);
    white-space: nowrap;
  }
  .price__unit {
    font-size: 30px;
    font-weight: 400;
  }
  .cta {
    position: absolute;
    left: 798px;
    top: 74px;
    width: 124px;
    height: 50px;
    border-radius: 8px;
    background: linear-gradient(180deg, var(--button-top), var(--button-bottom));
    box-shadow: 0 2px 4px rgba(0,0,0,0.7), inset 0 1px 0 rgba(255,255,255,0.25);
    font-family: "Roboto Condensed", sans-serif;
    font-weight: 700;
    font-size: 17px;
    line-height: 50px;
    text-align: center;
    color: #ffffff;
    text-decoration: none;
    letter-spacing: 0.2px;
  }
  .flag {
    position: absolute;
    display: block;
    box-shadow: 1px 2px 3px rgba(0,0,0,0.6);
  }
  .flag--usa     { left: 774px;  top: 9px;  width: 74px; height: 39px; }
  .flag--germany { left: 859px;  top: 9px;  width: 83px; height: 39px; }
  .flag--canada  { left: 954px;  top: 9px;  width: 84px; height: 39px; }
  .flag--spain   { left: 1050px; top: 9px;  width: 73px; height: 39px; }
  .flag--uk      { left: 996px;  top: 92px; width: 58px; height: 39px; }
  .flag--france  { left: 1067px; top: 92px; width: 56px; height: 39px; }
</style>
</head>
<body>
  <section class="banner" aria-label="Virtual Private Servers from $5 per month">
    <div class="banner__texture" role="img" aria-label="Dark hexagon mesh background"></div>

    <h1 class="headline">Virtual Private Servers</h1>
    <p class="features">Linux and Windows - 24/7 Free support - All panels - Root Access - High speed -<br>Uptime 99.9% - Instant Setup - Dedicated Bandwidth</p>

    <svg class="sticker" viewBox="0 0 112 112" aria-hidden="true">
      <defs>
        <radialGradient id="sticker-face" cx="40%" cy="40%" r="65%">
          <stop offset="0%" stop-color="var(--sticker-light)"/>
          <stop offset="70%" stop-color="#ececec"/>
          <stop offset="100%" stop-color="var(--sticker-shade)"/>
        </radialGradient>
        <linearGradient id="sticker-curl" x1="0" y1="0" x2="1" y2="1">
          <stop offset="0%" stop-color="#ffffff"/>
          <stop offset="100%" stop-color="#a9a9a9"/>
        </linearGradient>
      </defs>
      <path d="M56 4 A52 52 0 1 0 108 56 L84 56 Q86 30 84 22 Q72 20 56 28 Z" fill="url(#sticker-face)"/>
      <path d="M56 28 Q72 20 84 22 Q86 30 84 56 L108 56 A52 52 0 0 0 56 4 Z" fill="#000000" opacity="0.35"/>
      <path d="M56 28 Q72 20 84 22 Q86 30 84 56 Q96 40 104 30 Q82 14 56 28 Z" fill="url(#sticker-curl)"/>
    </svg>
    <span class="price__from">from</span>
    <span class="price__amount">$5<span class="price__unit">/mo</span></span>

    <svg class="flag flag--usa" viewBox="0 0 74 39" role="img" aria-label="USA">
      <rect width="74" height="39" fill="var(--flag-white)"/>
      <g fill="var(--flag-red)">
        <rect y="0" width="74" height="3"/><rect y="6" width="74" height="3"/>
        <rect y="12" width="74" height="3"/><rect y="18" width="74" height="3"/>
        <rect y="24" width="74" height="3"/><rect y="30" width="74" height="3"/>
        <rect y="36" width="74" height="3"/>
      </g>
      <rect width="30" height="21" fill="var(--flag-blue)"/>
    </svg>

    <svg class="flag flag--germany" viewBox="0 0 83 39" role="img" aria-label="Germany">
      <rect width="83" height="13" fill="var(--flag-black)"/>
      <rect y="13" width="83" height="13" fill="var(--flag-red)"/>
      <rect y="26" width="83" height="13" fill="var(--flag-gold)"/>
    </svg>

    <svg class="flag flag--canada" viewBox="0 0 84 39" role="img" aria-label="Canada">
      <rect width="84" height="39" fill="var(--flag-white)"/>
      <rect width="21" height="39" fill="var(--flag-red)"/>
      <rect x="63" width="21" height="39" fill="var(--flag-red)"/>
    </svg>

    <svg class="flag flag--spain" viewBox="0 0 73 39" role="img" aria-label="Spain">
      <rect width="73" height="39" fill="var(--flag-spain-red)"/>
      <rect y="10" width="73" height="19" fill="var(--flag-spain-yellow)"/>
    </svg>

    <svg class="flag flag--uk" viewBox="0 0 58 39" role="img" aria-label="United Kingdom">
      <rect width="58" height="39" fill="var(--flag-navy)"/>
      <path d="M0 0 L58 39 M58 0 L0 39" stroke="var(--flag-white)" stroke-width="8"/>
      <path d="M0 0 L58 39 M58 0 L0 39" stroke="var(--flag-red)" stroke-width="3"/>
      <path d="M29 0 V39 M0 19.5 H58" stroke="var(--flag-white)" stroke-width="12"/>
      <path d="M29 0 V39 M0 19.5 H58" stroke="var(--flag-red)" stroke-width="7"/>
    </svg>

    <svg class="flag flag--france" viewBox="0 0 56 39" role="img" aria-label="France">
      <rect width="19" height="39" fill="var(--flag-french-blue)"/>
      <rect x="19" width="18" height="39" fill="var(--flag-white)"/>
      <rect x="37" width="19" height="39" fill="var(--flag-french-red)"/>
    </svg>

    <a class="cta" href="#">CLICK HERE</a>
  </section>
</body>
</html>
```